Modern HomePage Design for Church

We are looking for a modern homepage design using the sections we put together in the template. The colors we want are blue, black, grey, and white. We do not want use the colors in the logo. Please modify the logo color to match the website color scheme.

Target Market(s)

Church

Industry/Entity Type

Church

Number of Pages Required

1 page

Colors
0293ce
ffffff
474747
9d9d9d

```html
<!DOCTYPE html>
<html lang="en">
<head>
<meta charset="utf-8">
<title>Grace Chapel – Home</title>
<link href="https://fonts.googleapis.com/css2?family=Cormorant+Garamond:wght@500;600&family=Cormorant+SC:wght@500;600;700&family=Montserrat:wght@400&display=swap" rel="stylesheet">
<style>
:root{
  --blue:#0293ce;
  --blue-deep:#01628a;
  --white:#ffffff;
  --dark:#474747;
  --grey:#9d9d9d;
  --black:#000000;
  --hero-top:#3a3a3a;
  --hero-bottom:#141414;
}
*{margin:0;padding:0;box-sizing:border-box}
html,body{width:1200px;height:1200px;overflow:hidden;background:var(--white)}
body{position:relative;font-family:'Cormorant SC',serif;color:var(--white)}
.page{position:absolute;left:82px;top:0;width:1037px;height:1200px;background:var(--white)}
.abs{position:absolute}

/* hero */
.hero{left:0;top:0;width:1037px;height:312px;
  background:radial-gradient(ellipse at 55% 40%,var(--dark) 0%,var(--hero-top) 40%,var(--hero-bottom) 100%)}
.section-label{display:flex;align-items:center;gap:8px;font-size:19px;font-weight:600;letter-spacing:.5px}
.section-label::before{content:"";width:44px;height:2px;background:var(--white)}
.pastor-photo{left:38px;top:70px;width:180px;height:204px;
  background:linear-gradient(180deg,var(--blue) 0 13%,var(--dark) 13% 100%)}
.quote{left:233px;top:72px;width:360px;font-size:16px;line-height:27px;font-weight:600;white-space:nowrap}
.quote .author{font-family:'Cormorant Garamond',serif;font-weight:600}
.pastor-text{left:233px;top:140px;width:270px;font-size:9px;line-height:26px;font-weight:600}
.podcasts{left:658px;top:67px;width:312px}
.podcast{height:69px;display:flex;align-items:center;padding-left:15px}
.podcast.lit{background:rgba(255,255,255,.13)}
.podcast svg{flex:none}
.podcast p{margin-left:22px;font-size:13px;line-height:30px;font-weight:600}
.podcast p span{font-size:14px}

/* events */
.events-title{left:0;width:1037px;top:334px;text-align:center;color:var(--black)}
.events-title h1{font-size:40px;font-weight:600;line-height:44px}
.events-title h2{font-size:17px;font-weight:600;line-height:18px}
.event{left:69px;width:898px;height:189px;display:flex}
.event .photo{width:377px;height:100%;position:relative;
  background:radial-gradient(ellipse at 60% 40%,#7fc6e6 0%,var(--blue) 30%,var(--dark) 70%,var(--black) 100%)}
.event .badge{position:absolute;left:28px;top:0;width:67px;height:58px;text-align:center;font-weight:600}
.badge .day{font-size:25px;line-height:34px}
.badge .month{font-size:13px;line-height:16px}
.event .info{flex:1;position:relative;padding:28px 0 0 35px}
.info h3{font-size:25px;font-weight:700;line-height:30px;margin-bottom:4px}
.row{display:flex;align-items:center;height:33px;font-size:18px;font-weight:600}
.row svg{width:22px;height:22px;margin-right:15px}
.read-more{position:absolute;right:43px;top:135px;width:103px;height:28px;border:2px solid var(--black);
  color:var(--black);font-family:'Cormorant Garamond',serif;font-size:18px;text-align:center;line-height:24px;font-weight:600}
.event.one .info{background:var(--blue)}
.event.one .badge{background:var(--blue-deep)}
.event.two .info{background:var(--grey)}
.event.two .badge{background:var(--dark)}
.event.two .row{font-size:22px}

/* footer */
.footer{left:0;top:914px;width:1037px;height:258px;background:var(--black)}
.footer .section-label{color:var(--blue);font-size:18px}
.card{width:254px;height:68px;background:var(--grey);text-align:center;padding-top:7px;margin-bottom:3px}
.card h4{font-size:14px;font-weight:600;line-height:20px}
.card p{font-family:'Montserrat',sans-serif;font-size:10px;line-height:14px;color:#eee}
.tags-title{left:398px;top:26px;width:239px;text-align:center;font-size:18px;font-weight:600}
.tags{left:398px;top:49px;display:flex;gap:3px}
.tags span{width:78px;height:28px;background:var(--blue);text-align:center;font-size:19px;line-height:28px;font-weight:600;letter-spacing:1px}
.feed{left:399px;top:84px;width:238px;height:112px;display:flex;align-items:center;justify-content:center;
  background:linear-gradient(180deg,var(--dark) 0%,var(--grey) 50%,var(--blue) 72%,var(--black) 100%);font-size:20px;font-weight:600}
.copyright{left:0;top:1172px;width:1037px;height:28px;text-align:center;line-height:28px;
  font-family:'Montserrat',sans-serif;font-size:12px;color:var(--black)}
</style>
</head>
<body>
<div class="page">

  <section class="abs hero" role="img" aria-label="Church interior with a crucifix, softly lit">
    <div class="abs section-label" style="left:38px;top:38px">Pastor</div>
    <div class="abs pastor-photo" role="img" aria-label="Portrait of the pastor speaking into a microphone"></div>
    <p class="abs quote">"Your prayers at midnight must command<br>your miracles at daybreak!"-<span class="author">Pastor Dele Amos</span></p>
    <p class="abs pastor-text">Lorem ipsum dolor sit amet, consectetuer adipiscing elit, sed diam nonummy nibh euismod tincidunt ut laoreet dolore magna aliquam erat volutpat. Ut wisi enim ad</p>

    <div class="abs section-label" style="left:658px;top:36px">Podcasts</div>
    <div class="abs podcasts">
      <div class="podcast lit">
        <svg width="48" height="48" viewBox="0 0 48 48"><circle cx="24" cy="24" r="22" fill="none" stroke="rgba(255,255,255,.35)" stroke-width="3"/><path d="M20 18l10 6-10 6z" fill="rgba(255,255,255,.35)"/></svg>
        <p>Lorem ipsum dolor sit amet,<br><span>by Pastor X</span></p>
      </div>
      <div class="podcast">
        <svg width="48" height="48" viewBox="0 0 48 48"><circle cx="24" cy="24" r="22" fill="none" stroke="rgba(255,255,255,.35)" stroke-width="3"/><path d="M20 18l10 6-10 6z" fill="rgba(255,255,255,.35)"/></svg>
        <p>Lorem ipsum dolor sit amet,<br><span>by Pastor X</span></p>
      </div>
      <div class="podcast lit">
        <svg width="48" height="48" viewBox="0 0 48 48"><circle cx="24" cy="24" r="22" fill="none" stroke="rgba(255,255,255,.35)" stroke-width="3"/><path d="M20 18l10 6-10 6z" fill="rgba(255,255,255,.35)"/></svg>
        <p>Lorem ipsum dolor sit amet,<br><span>by Pastor X</span></p>
      </div>
    </div>
  </section>

  <header class="abs events-title">
    <h1>Upcoming Events</h1>
    <h2>Experience God's Presence</h2>
  </header>

  <article class="abs event one" style="top:461px">
    <div class="photo" role="img" aria-label="Worship crowd with raised hands before a lit stage">
      <div class="badge"><div class="day">22nd</div><div class="month">Feb, 2019</div></div>
    </div>
    <div class="info">
      <h3>Event's Name</h3>
      <div class="row"><svg viewBox="0 0 24 24" fill="none" stroke="#000" stroke-width="2"><circle cx="12" cy="12" r="10"/><path d="M12 6v6l4 2"/></svg>Sunday, 00:00 am to 00:00 am</div>
      <div class="row"><svg viewBox="0 0 24 24"><path d="M12 2L1 12h3v10h16V12h3z" fill="#000"/><path d="M12 10v8M9 13h6" stroke="#fff" stroke-width="2"/></svg>Church's Name</div>
      <div class="row"><svg viewBox="0 0 24 24" fill="none" stroke="#000" stroke-width="1.6"><path d="M12 22s-7-7.5-7-13a7 7 0 0114 0c0 5.5-7 13-7 13z"/><circle cx="12" cy="9" r="2.5"/></svg>Address</div>
      <div class="read-more">Read More</div>
    </div>
  </article>

  <article class="abs event two" style="top:666px">
    <div class="photo" role="img" aria-label="Worship crowd with raised hands before a lit stage">
      <div class="badge"><div class="day">23rd</div><div class="month">Feb, 2019</div></div>
    </div>
    <div class="info">
      <h3>Event's Name</h3>
      <div class="row"><svg viewBox="0 0 24 24" fill="none" stroke="#000" stroke-width="2"><circle cx="12" cy="12" r="10"/><path d="M12 6v6l4 2"/></svg>Sunday, 00:00 am to 00:00 am</div>
      <div class="row"><svg viewBox="0 0 24 24"><path d="M12 2L1 12h3v10h16V12h3z" fill="#000"/><path d="M12 10v8M9 13h6" stroke="#fff" stroke-width="2"/></svg>Church's Name</div>
      <div class="row"><svg viewBox="0 0 24 24" fill="none" stroke="#000" stroke-width="1.6"><path d="M12 22s-7-7.5-7-13a7 7 0 0114 0c0 5.5-7 13-7 13z"/><circle cx="12" cy="9" r="2.5"/></svg>Address</div>
      <div class="read-more">Read More</div>
    </div>
  </article>

  <footer class="abs footer">
    <div class="abs section-label" style="left:47px;top:28px">Latest news</div>
    <div class="abs" style="left:47px;top:54px">
      <div class="card"><h4>Lorem ipsum dolor sit</h4><p>Lorem ipsum dolor sit amet, con-<br>sectetuer adipiscing elit, sed diam</p></div>
      <div class="card"><h4>Lorem ipsum dolor sit</h4><p>Lorem ipsum dolor sit amet, con-<br>sectetuer adipiscing elit, sed diam</p></div>
    </div>

    <div class="abs tags-title">Sermons tags</div>
    <div class="abs tags"><span>TAGS</span><span>TAGS</span><span>TAGS</span></div>
    <div class="abs feed" role="img" aria-label="Wooden cross against a sunset sky">PODSTREAM FEED</div>

    <div class="abs section-label" style="left:735px;top:28px">Latest Semons</div>
    <div class="abs" style="left:735px;top:54px">
      <div class="card"><h4>Lorem ipsum dolor sit</h4><p>Lorem ipsum dolor sit amet, con-<br>sectetuer adipiscing elit, sed diam</p></div>
      <div class="card"><h4>Lorem ipsum dolor sit</h4><p>Lorem ipsum dolor sit amet, con-<br>sectetuer adipiscing elit, sed diam</p></div>
    </div>
  </footer>

  <div class="abs copyright">© 2019 website | Powered by website</div>
</div>
</body>
</html>
```